hotel's Website

Hotels website redesign for reference pictures, logo etc see http://restwellmarlow.co.uk/

1. 2-3 Special offers on the main page.
2. Booking calender
3. Location Map
4. Picture gallery.
5. Journeyscope reviews.
6. short description
7. Social Media sharing.
8 Phone number and address.

Industry/Entity Type

Hotel

Requirements
Must have
• 1. 2-3 Special offers on the main page.
2. Booking calender
3. Location Map
4. Picture gallery.
5. Journeyscope reviews.
6. short description
7. Social Media sharing.

```html
<!DOCTYPE html>
<html lang="en">
<head>
<meta charset="utf-8">
<title>Restwell London - Victoria</title>
<link href="https://fonts.googleapis.com/css2?family=Tinos&family=Arimo&family=Great+Vibes&display=swap" rel="stylesheet">
<style>
:root{
  --bg:#000;
  --text:#fff;
  --muted:#c4c4c4;
  --link:#a9d6ff;
  --rule:#2e2e2e;
  --brand-blue:#0a6fb8;
  --nav-top:#bfe6f6;
  --nav-bottom:#3aa0cf;
  --btn-dark-top:#25495a;
  --btn-dark-bottom:#0c2230;
  --field-top:#6a6a6a;
  --field-mid:#b9b9b9;
  --footer-top:#1f4f66;
  --footer-bottom:#0a2838;
}
*{margin:0;padding:0;box-sizing:border-box}
html,body{width:1200px;height:1000px;overflow:hidden;background:var(--bg)}
body{position:relative;font-family:'Tinos',serif;color:var(--text)}
.abs{position:absolute}

.brand-block{left:108px;top:0;width:350px;height:126px;background:var(--bg)}
.brand-square{left:138px;top:30px;width:60px;height:68px;background:var(--brand-blue)}
.brand-name{left:138px;top:108px;font-size:9px;letter-spacing:2.5px;color:#ddd}
.brand-divider{left:238px;top:32px;width:1px;height:66px;background:#bbb}
.brand-location{left:253px;top:54px;font-family:'Arimo',sans-serif;font-size:18px}

.contact{left:770px;top:9px;font-size:11px;line-height:20px}

.main-nav{left:480px;top:69px;width:515px;height:25px;display:flex;background:linear-gradient(var(--nav-top),var(--nav-bottom));font-size:10px}
.main-nav a{color:#fff;text-decoration:none;display:flex;align-items:center;justify-content:center;height:100%}
.main-nav .current{width:64px;background:linear-gradient(#e6f6fc,#8fd0ea);font-size:13px}

.hero{left:108px;top:96px;width:972px;height:206px;background:linear-gradient(100deg,#4a4540 0%,#8a6a3a 25%,#d9c07a 45%,#b8a890 60%,#d98b58 78%,#caa65a 100%)}
.hero-arrow{top:160px}

.about-title{left:143px;top:338px;font-family:'Great Vibes',cursive;font-size:36px}
.about-text{left:143px;top:402px;width:490px;font-size:19px;line-height:26.5px;color:var(--muted)}
.about-rule{left:124px;top:568px;width:559px;height:1px;background:var(--rule)}
.column-rule{left:720px;top:393px;width:1px;height:383px;background:var(--rule)}

.offer{top:609px;width:150px}
.offer-photo{width:150px;height:77px;position:relative}
.offer-caption{position:absolute;left:0;bottom:0;width:100%;height:22px;background:rgba(0,0,0,.45);font-size:13px;text-align:center;line-height:22px}
.offer-text{margin:11px 0 0 6px;width:142px;font-size:13px;line-height:13.5px;color:#eee}
.read-more{display:block;margin:11px auto 0;width:90px;height:19px;background:linear-gradient(var(--btn-dark-top),var(--btn-dark-bottom));border:1px solid #3d6678;color:#9cc4d8;font-size:13px;text-align:center;line-height:17px}

.book-title{left:720px;top:338px;width:340px;text-align:center;font-size:23px}
.field-label{font-size:18px}
.field{background:linear-gradient(var(--field-top),var(--field-mid) 45%,#9a9a9a);border:1px solid #555}
.search-btn{left:823px;top:548px;width:144px;height:33px;background:linear-gradient(#7fc9ef,#2a8fc4);color:#e8f2f8;font-size:20px;text-align:center;line-height:33px;border:1px solid #5aaedb}
.map{left:758px;top:609px;width:284px;height:79px;background:linear-gradient(160deg,#e8ecdc,#cfe0c0 50%,#e3e6da)}

.social{top:748px;width:30px;height:30px;border-radius:2px}

.section-title{font-size:17px}
.partners-note{left:139px;top:818px;width:260px;font-size:10px;line-height:13px;color:#ddd}
.partners-list{left:139px;top:861px;list-style:none;font-size:13px;line-height:13.4px;color:var(--link)}
.review-name{left:460px;top:856px;font-size:34px;display:flex;align-items:center;gap:10px}
.review-dot{width:34px;height:34px;border-radius:50%;background:#fff}
.newsletter-text{left:793px;top:817px;width:270px;font-size:13px;line-height:12.5px;color:#bbb}
.email-field{left:762px;top:861px;width:291px;height:34px;font-size:17px;color:#222;padding-left:16px;line-height:36px}
.subscribe-btn{left:856px;top:907px;width:90px;height:27px;background:linear-gradient(var(--btn-dark-top),var(--btn-dark-bottom));border:1px solid #3d6678;font-size:13px;text-align:center;line-height:25px}

.site-footer{left:0;top:970px;width:1200px;height:30px;background:linear-gradient(var(--footer-top),var(--footer-bottom));font-size:13px;text-align:center;line-height:28px}
</style>
</head>
<body>

<header>
  <div class="abs brand-block"></div>
  <div class="abs brand-square"></div>
  <div class="abs brand-name">RESTWELL HOTELS</div>
  <div class="abs brand-divider"></div>
  <div class="abs brand-location">London - Victoria</div>

  <address class="abs contact" style="font-style:normal">
    Ashgrove Lane, Victoria London SW9 4ZX 12-16<br>
    stay@restwellmarlow.co.uk<br>
    Tel: + 44 (0) 20 7946 0101 | Fax:+ 44 (0) 20 7946 0102
  </address>

  <nav class="abs main-nav">
    <a class="current" href="#">Home</a>
    <a href="#" style="width:64px">Our Rooms</a>
    <a href="#" style="width:62px">Attractions</a>
    <a href="#" style="width:62px">London Events</a>
    <a href="#" style="width:68px">Special Offers</a>
    <a href="#" style="width:64px">Photos</a>
    <a href="#" style="width:64px">Directions</a>
    <a href="#" style="width:60px">Contact</a>
  </nav>
</header>

<section class="abs hero" role="img" aria-label="Photo gallery: modern hotel lounge with yellow armchairs and a glass coffee table"></section>
<svg class="abs hero-arrow" style="left:120px" width="30" height="88" viewBox="0 0 30 88"><polygon points="30,0 0,44 30,88 22,44" fill="#cfcfcf"/></svg>
<svg class="abs hero-arrow" style="left:1033px" width="30" height="88" viewBox="0 0 30 88"><polygon points="0,0 30,44 0,88 8,44" fill="#cfcfcf"/></svg>

<main>
  <h1 class="abs about-title" style="font-weight:normal">A Few Words About Us</h1>
  <p class="abs about-text">,Lorem ipsum dolor sit amet, consectetur adipisicing elit sed do eiusmod tempor incididunt ut labore et dolor magna aliqua. Ut enim ad minim veniam, quis nostrud exercitation ullamco laboris nisi ut aliquip ex ea .commodo consequat</p>
  <div class="abs about-rule"></div>
  <div class="abs column-rule"></div>

  <article class="abs offer" style="left:138px">
    <div class="offer-photo" role="img" aria-label="London clock tower at night with light trails" style="background:linear-gradient(135deg,#1a2a6a,#5a4a8a 50%,#c09050)">
      <div class="offer-caption">Special Offers</div>
    </div>
    <p class="offer-text">Lorem ipsum dolor sit amet, consectetur adipi sicing elit, sed do</p>
    <a class="read-more" href="#">Read More</a>
  </article>
  <article class="abs offer" style="left:327px">
    <div class="offer-photo" role="img" aria-label="London skyline with observation wheel at dusk" style="background:linear-gradient(180deg,#3a3a6a,#8a5a7a 55%,#c08040)">
      <div class="offer-caption">Explore London</div>
    </div>
    <p class="offer-text">Lorem ipsum dolor sit amet, consectetur adipi sicing elit, sed do</p>
    <a class="read-more" href="#">Read More</a>
  </article>
  <article class="abs offer" style="left:518px">
    <div class="offer-photo" role="img" aria-label="Hotel bedroom with warm lighting" style="background:linear-gradient(160deg,#e0c080,#b08050 55%,#6a3a2a)">
      <div class="offer-caption">Stay in Comfort</div>
    </div>
    <p class="offer-text">Lorem ipsum dolor sit amet, consectetur adipi sicing elit, sed do</p>
    <a class="read-more" href="#">Read More</a>
  </article>

  <aside>
    <h2 class="abs book-title" style="font-weight:normal">Book a room</h2>
    <div class="abs field-label" style="left:759px;top:392px">Room</div>
    <div class="abs field" style="left:752px;top:417px;width:291px;height:34px"></div>
    <div class="abs field-label" style="left:759px;top:462px">From</div>
    <div class="abs field-label" style="left:923px;top:462px">To</div>
    <div class="abs field" style="left:753px;top:489px;width:128px;height:34px"></div>
    <div class="abs field" style="left:915px;top:489px;width:128px;height:34px"></div>
    <div class="abs search-btn">Search</div>
    <div class="abs map" role="img" aria-label="Location map of the hotel area"></div>

    <div class="abs social" style="left:807px;background:#3b5998"></div>
    <div class="abs social" style="left:847px;background:#d34836"></div>
    <div class="abs social" style="left:887px;background:#2c8fcf"></div>
    <div class="abs social" style="left:928px;background:#5a8a3a"></div>
    <div class="abs social" style="left:969px;background:#d8282e"></div>
  </aside>
</main>

<section>
  <h3 class="abs section-title" style="left:139px;top:791px;font-weight:normal">Partner Hotels</h3>
  <p class="abs partners-note">This hotel is owned and operated by the Linden Hotel Group, please take a look of some of our other hotels :below</p>
  <ul class="abs partners-list">
    <li>Maplestay London - Camden Lock</li>
    <li>Maplestay Express - Earls Court</li>
    <li>Foxley House Hotel</li>
    <li>brightRoom Victoria</li>
    <li>brightRoom Paddington</li>
    <li>Restwell Suites - King's Cross</li>
  </ul>

  <h3 class="abs section-title" style="left:528px;top:792px;font-weight:normal">Journeyscope</h3>
  <div class="abs review-name"><span class="review-dot"></span>Journeyscope</div>

  <h3 class="abs section-title" style="left:793px;top:792px;font-weight:normal">Stay in Touch</h3>
  <p class="abs newsletter-text">Sign up for our newsletter for latest news from Restwell London - Victoria</p>
  <div class="abs field email-field">Email Address</div>
  <div class="abs subscribe-btn">Subscribe</div>
</section>

<footer class="abs site-footer">.All rights reserved .2013 ©</footer>

</body>
</html>
```